PowerPoint Design Project

Powerpoint design for an online marketing agency.
PP will be used as a WhitePaper to showcase our expertise.
Our USP is that we use data for marketing so the design must reflect this with charts and graphs.
A set of images is available in our flickr account
http://www.pixelvault.example/photos/kelmora/sets/48302916574021983/with/3104827561/
We already have written real content for the PP for you to work with.
Updates

1. I have added a sample of the content a 2-page extract in a word document. The full document is around 15 pages.
2. While the finished piece is to be in PowerPoint format, it will also be used as a White Paper so the design should reflect this - i.e it should be able to be read like it was a well designed Word document not just a PP
3. The design you see in the sample 2-page document is just for illustration purposes it is not intended to influence the final design at all. So for example it currently has some pull-quotes in black boxes - that is just to show what they are and I don't want the final piece to have black boxes around quotes.
4. I've been asked to make this project guaranteed: as this is the first time I've used ArtHivePro I'm going to keep it as a standard project but we are committed to the work.
5. The current deadline is for the START of design work. We need the completed design by 21 September, so there is plenty of time to schedule this in with your other work.
Many thanks
Nigel 

The designs shown so far would not be suitable for turning into a WhitePaper. For example the bars across the top of the design create a break at the start of each page rather than emphasise the continuous nature of the document. 

Here is an example of some great design for a similar project - and we've uploaded another sample as a file

http://www.surgeloft.example/downloads/[SURGE]-what-its-like-working-

If you asked me for some ideas on the feel of the design I would say:

1. Bold - it has to look interesting - corporate world but it doesn't need to feel dull/grey
2. Exciting 
3. Precise - easy to read , not a fussy design

Target Market(s)

Business developers, sales managers, CEOs of companies with over 5 employees but without their own marketing department

Industry/Entity Type

Marketing

Requirements
Must have
• Flawless design that says "this company is smart and means business"
Nice to have
• the powerpoint should lend itself to easy file/saveas to be delivered as a PDF and for individual slides to be extracted for presentation, or use as images in blog posts etc (so for example any page number must be easy to remove).
Should not have
• no cartoons, no line drawings, nothing to obscure easy legibility

```html
<!DOCTYPE html>
<html lang="en">
<head>
<meta charset="utf-8">
<title>How to Run a Successful Data Driven Marketing Campaign</title>
<link rel="stylesheet" href="https://fonts.googleapis.com/css2?family=Alfa+Slab+One&family=Montserrat:wght@600&family=Open+Sans:wght@300;700&display=swap">
<style>
  :root {
    --bg-deep: #343437;
    --bg-mid: #58585c;
    --bg-light: #7a7a7f;
    --brand-blue: #1d4f9c;
    --title-blue: #1b3d86;
    --title-edge: #d6e0f2;
    --accent-blue: #2a9ad8;
    --body-text: #ededed;
    --rule-grey: #8a8a8e;
    --banner-blue: #123e86;
    --banner-edge: #2f7fd0;
    --white: #ffffff;
  }
  * { margin: 0; padding: 0; box-sizing: border-box; }
  html, body { width: 1200px; height: 903px; overflow: hidden; }
  body {
    position: relative;
    background: linear-gradient(118deg, var(--bg-deep) 0%, var(--bg-mid) 28%, var(--bg-light) 47%, var(--bg-mid) 66%, var(--bg-deep) 100%);
    font-family: "Open Sans", Arial, sans-serif;
    font-weight: 300;
    color: var(--body-text);
  }
  .brand {
    position: absolute; left: 60px; top: 50px;
    display: flex; align-items: center; gap: 10px;
  }
  .brand-mark { width: 22px; height: 22px; background: var(--brand-blue); }
  .brand-name {
    font-weight: 700; font-size: 48px; line-height: 52px;
    color: var(--brand-blue); letter-spacing: -1px;
  }
  .slide-title {
    position: absolute; left: 294px; top: 38px; white-space: nowrap;
    font-family: "Alfa Slab One", Georgia, serif; font-weight: 400;
    font-size: 44px; line-height: 40px; color: var(--title-blue);
    -webkit-text-stroke: 1px var(--title-edge);
  }
  .header-rule { position: absolute; left: 58px; top: 158px; width: 1097px; height: 6px; }
  .header-rule .accent { position: absolute; left: 0; top: 0; width: 205px; height: 6px; background: var(--brand-blue); }
  .header-rule .thin { position: absolute; left: 205px; top: 3px; right: 0; height: 1px; background: var(--rule-grey); }

  .section-heading {
    position: absolute; left: 70px; top: 226px; white-space: nowrap;
    font-weight: 300; font-size: 26px; line-height: 34px; color: var(--accent-blue);
  }
  .copy {
    position: absolute; left: 70px; white-space: nowrap;
    font-size: 22px; line-height: 27px;
  }
  .intro { top: 282px; }
  .summary { top: 585px; }
  .closing { top: 760px; }
  .benefits { position: absolute; left: 70px; top: 439px; list-style: none; }
  .benefits li {
    position: relative; padding-left: 32px; white-space: nowrap;
    font-size: 22px; line-height: 27px; margin-bottom: 21px;
  }
  .benefits li::before {
    content: ""; position: absolute; left: 3px; top: 8px;
    width: 7px; height: 12px; background: var(--accent-blue);
    border-radius: 0 7px 7px 0;
  }
  .benefits .key { color: var(--accent-blue); }

  .pull-quote { position: absolute; left: 66px; top: 660px; width: 1046px; height: 77px; }
  .pull-quote svg { position: absolute; inset: 0; }
  .pull-quote blockquote {
    position: absolute; left: 14px; top: 14px; white-space: nowrap;
    font-family: "Montserrat", Arial, sans-serif; font-weight: 600;
    font-size: 25px; line-height: 23px; color: var(--white); letter-spacing: -0.4px;
  }
  .page-number { position: absolute; left: 998px; top: 854px; font-size: 18px; color: var(--rule-grey); }
  .page-hatch { position: absolute; left: 1024px; top: 860px; width: 124px; height: 14px; }
</style>
</head>
<body>
  <div class="brand">
    <span class="brand-mark"></span>
    <span class="brand-name">kelmora</span>
  </div>
  <h1 class="slide-title">How to Run a Successful Data<br>Driven Marketing Campaign</h1>
  <div class="header-rule"><span class="accent"></span><span class="thin"></span></div>

  <h2 class="section-heading">Create Remarkable Content that People Want to Receive and Share</h2>
  <p class="copy intro">The modern science of marketing uses a new and scientific approach to the way businesses<br>market their products for profit. Combining marketing expertise, statistical data, and psychological<br>research from behavioural economics, the science of marketing explains how companies can use<br>21st century marketing strategies like blogging, social media and permission-based email<br>marketing to:</p>
  <ul class="benefits">
    <li><span class="key">Know what works in marketing</span>, based on interpreting measurable statistical data</li>
    <li><span class="key">Target marketing budgets</span> for highest impact using evidence of return on investment</li>
    <li><span class="key">Adapt marketing campaigns in real-time</span> based on actual customer behaviour.</li>
  </ul>
  <p class="copy summary">The science of marketing gives you the research and tools to deliver scientific marketing that<br>works, based on data you can prove.</p>

  <figure class="pull-quote">
    <svg width="1046" height="77" viewBox="0 0 1046 77">
      <polygon points="0,0 1046,0 1006,38.5 1046,77 0,77" fill="var(--banner-edge)"/>
      <polygon points="5,5 1032,5 997,38.5 1032,72 5,72" fill="var(--banner-blue)"/>
    </svg>
    <blockquote>No longer are size and budget the deciding factors. Now speed and<br>agility are decisive competitive advantage – Daniel Mercer Holt.</blockquote>
  </figure>

  <p class="copy closing">Now you know what the science of marketing is, how can you design a marketing campaign that<br>(to use an Americanism) rocks your ROI?</p>

  <span class="page-number">2</span>
  <svg class="page-hatch" viewBox="0 0 124 14" aria-hidden="true">
    <defs>
      <pattern id="hatch" width="6" height="14" patternUnits="userSpaceOnUse" patternTransform="skewX(-30)">
        <rect width="3" height="14" fill="var(--brand-blue)"/>
      </pattern>
    </defs>
    <rect width="124" height="14" fill="url(#hatch)"/>
  </svg>
</body>
</html>
```